Creative, Modern and Conversion based Web Design

Kovel Digital has recently launched a new logo and as part of our companies rebranding, we need a new website aimed towards the UK B2B marketplace.

The website needs to deliver a modern and creative website design whilst ensuring the design is tailored towards conversion optimisation.

This site must drive point of contact either from an online form, via a direct telephone call or Skype connection.

Our sales are all offline so the website will be a simple, elegant and stunning information portal.

Kovel Digital offers Digital Marketing services to companies throughout the UK - our target audiences are companies that turnover a minimum of 3 million pounds a year and as such we need to deliver a professional image that installs confidence in our companies abilities.

We do not like websites that are reliant upon stock photography - we are happy for stock photography to be used in a small way however the site must not look like a template filled with stock photography.

What do we do

We supply digital marketing services to those companies who demand a strong return on investment - our company prides itself on delivering successful campaigns that help establish long-term profitable relationships.

A lot of the information presented on our old site is relevant today however the design sucks. So please use the information on our current website as a foundation for your design content.

I am looking for several page designs including

"Home Page" Desktop Version
"Service Page" Desktop Version
"Blog Page" Desktop Version

"Home Page" Mobile Version
"Service Page" Mobile Version
"Blog Page" Mobile Version

In the 1st instance please only submit a single design for the "Home Page" Desktop Version - those designers that we are impressed with will be asked to complete the other designs before a winner is selected.

I like modern clean fonts - the site needs to welcome the reader and encourage them to absorb the information - not to overload and make them leave.

The site must be designed to naturally fit our companies new logo.

NO TEMPLATES

Target Market(s)

B2b - 3 million turnover and above

Industry/Entity Type

Digital Marketing

Number of Pages Required

3 page

Requirements
Must have
• Blended well with the companies logo
• We need conversion optimisation to be a huge part of the design - we considered a conversation when a potential customer reaches out to use via - web form, telephone or skype
• The current content on the old website fits today's business but the design sucks.
• www.koveldigital-studio.net
Nice to have
• We need 3 pages (in 2 variants Desktop and Mobile)
• Home Page
• Service Page
• Blog Page
• Please only deliver the "Home Page" desktop version - if we are happy with your design we will aks for the additional pages
Should not have
• No templates and not stock photo heavy design

```html
<!DOCTYPE html>
<html lang="en">
<head>
<meta charset="utf-8">
<title>Kovel Digital – Search Marketing That Actually Delivers</title>
<link href="https://fonts.googleapis.com/css2?family=Lato:wght@300;400;700;900&family=Oswald:wght@500;700&display=swap" rel="stylesheet">
<style>
:root{
  --navy:#0b1830;
  --navy-2:#13284d;
  --blue:#0f4c9e;
  --blue-bright:#2a63c9;
  --purple:#6a1f8e;
  --purple-2:#5a1a9c;
  --lime:#c8f03c;
  --ink:#1c1c22;
  --text:#3a3a44;
  --muted:#8a8a96;
  --light:#f3f3f5;
  --white:#ffffff;
  --black:#0d0d0f;
}
*{box-sizing:border-box;margin:0;padding:0}
html,body{width:1200px;height:4401px;overflow:hidden}
body{font-family:"Lato",sans-serif;color:var(--text);background:var(--white);position:relative}
.abs{position:absolute}
section,header,footer{position:absolute;left:0;width:1200px}

/* header + hero */
.hero{top:0;height:1268px;background:var(--white)}
.hero-wave{position:absolute;top:0;right:0;width:760px;height:560px}
.brand{left:44px;top:40px;display:flex;align-items:center;gap:12px}
.brand-mark{width:26px;height:26px;background:var(--muted)}
.brand-name{font-weight:900;font-size:26px;color:#5c5c66;letter-spacing:1px;text-transform:uppercase}
.brand-sub{font-size:11px;color:var(--muted);letter-spacing:4px;margin-top:2px}
.phone{left:262px;top:68px;font-size:15px;color:#333;display:flex;align-items:center;gap:8px}
.nav{right:44px;top:62px;display:flex;align-items:center;gap:40px}
.nav a{color:var(--white);text-decoration:none;font-size:15px;letter-spacing:.5px}
.nav .nav-cta{border:2px solid var(--white);padding:8px 16px}
.hero-device{position:absolute;left:690px;top:160px;width:290px;height:470px;border-radius:40px;transform:rotate(-24deg);background:linear-gradient(160deg,#eef95a,#b6e43a 60%,#8ec22f);box-shadow:0 30px 60px rgba(0,0,0,.25)}
.hero-title{left:38px;top:238px;font-size:40px;font-weight:300;color:var(--ink);line-height:1.15}
.hero-lead{left:38px;top:342px;font-size:15px;color:#444;line-height:1.45;width:420px}
.btn{display:inline-block;text-decoration:none;font-weight:700;letter-spacing:.5px;font-size:15px}
.btn-quote{left:38px;top:418px;background:var(--blue);color:var(--white);padding:16px 40px;border-radius:30px}
.btn-how{left:312px;top:432px;color:var(--blue)}

/* ROI */
.roi-title{left:40px;top:692px;font-size:40px;font-weight:400;color:var(--ink);line-height:1.12}
.roi-kicker{left:40px;top:784px;font-size:22px;color:var(--muted);letter-spacing:1px}
.roi-body{left:40px;top:850px;width:765px;font-size:16px;line-height:1.42;color:#333;text-align:justify}
.roi-handle{left:40px;top:1035px;width:560px;font-size:16px;line-height:1.42;color:#333}
.roi-handle b{color:var(--purple)}
.roi-image{left:830px;top:850px;width:320px;height:240px;background:linear-gradient(135deg,#c8ccd6,#6c7180 60%,#2b2e36);border-radius:8px}
.roi-accent{right:0;top:1020px;width:200px;height:140px;border-radius:200px 0 0 0;background:var(--blue)}
.badges{left:44px;top:1126px;display:flex;gap:38px}
.badge{width:92px;height:44px;border-radius:6px;background:#d7d8dd}

/* services */
.services{top:1268px;height:1035px;background:linear-gradient(180deg,#0a1630 0%,#13284d 55%,#0c1a35 100%)}
.services-kicker{top:90px;width:100%;text-align:center;color:#c9d3e6;font-size:14px;letter-spacing:1px;text-transform:uppercase}
.services-title{top:110px;width:100%;text-align:center;color:var(--white);font-size:40px;font-weight:700}
.card{position:absolute;width:400px}
.card-icon{position:absolute;left:-140px;top:0;width:112px;height:112px;border-radius:50%;background:conic-gradient(var(--lime) 0 40%,var(--blue-bright) 40% 70%,#f2a22b 70% 100%)}
.card h3{color:var(--lime);font-size:34px;font-weight:400;margin-bottom:10px}
.card p{color:#e4e8f0;font-size:14px;line-height:1.38;width:340px}
.card .more{display:inline-block;margin-top:12px;background:var(--lime);color:var(--navy);font-size:13px;font-weight:700;padding:7px 24px;border-radius:20px}

/* grow */
.grow{top:2303px;height:632px;background:var(--white)}
.grow-title{right:47px;top:58px;font-size:40px;font-weight:700;color:var(--ink)}
.grow-kicker{right:47px;top:112px;font-size:13px;color:var(--muted);letter-spacing:2px;border-top:1px solid #bbb;padding-top:6px;width:410px;text-align:right}
.grow-text{left:108px;top:216px;width:432px;border-top:4px solid var(--ink);padding-top:22px;font-size:15px;line-height:1.45;color:#222}
.grow-text p+p{margin-top:16px}
.grow-photo{left:575px;top:180px;width:578px;height:410px;background:linear-gradient(135deg,#9aa6b3,#4b5663 50%,#c0b29e)}
.stats{left:108px;top:448px;display:flex;gap:6px}
.stat{width:150px;height:138px;background:var(--black);color:var(--white);text-align:center;padding-top:14px}
.stat b{font-family:"Oswald",sans-serif;font-size:62px;font-weight:700;line-height:1;display:block}
.stat span{font-family:"Oswald",sans-serif;font-size:14px;letter-spacing:3px;display:block;margin-top:8px;line-height:1.1}
.stat-tick{width:220px;height:138px;background:var(--light);display:flex;align-items:center;justify-content:center}

/* handle seo */
.handle{top:2935px;height:747px;background:var(--light)}
.handle-title{left:44px;top:72px;font-size:40px;font-weight:700;color:var(--ink)}
.handle-kicker{left:150px;top:126px;font-size:13px;color:var(--muted);letter-spacing:2px}
.handle-photo{left:44px;top:184px;width:581px;height:461px;background:linear-gradient(160deg,#dfe4ea,#9fb0c2 55%,#5d6b7c)}
.click-box{left:108px;top:504px;width:362px;height:141px;background:var(--black);color:var(--white);padding:26px 0 0 22px}
.click-box strong{font-family:"Oswald",sans-serif;font-size:44px;font-weight:700;display:block;line-height:1}
.click-box span{font-family:"Oswald",sans-serif;font-size:14px;letter-spacing:3px;display:block;margin-top:10px;line-height:1.25}
.click-arrow{left:470px;top:504px;width:155px;height:141px;background:#e4e4e8;display:flex;align-items:center;justify-content:center}
.handle-text{left:669px;top:128px;width:440px;border-top:4px solid var(--ink);padding-top:20px;font-size:14.5px;line-height:1.42;color:#222}
.handle-text p+p{margin-top:14px}

/* cta */
.cta{top:3682px;height:338px;background:var(--white);text-align:center}
.cta h2{position:absolute;top:148px;width:100%;font-size:32px;font-weight:700;color:var(--ink)}
.cta p{position:absolute;top:192px;width:100%;font-size:14px;color:#555}
.btn-contact{position:absolute;left:411px;top:226px;width:358px;background:var(--purple-2);color:var(--white);padding:12px 0;border-radius:8px;font-size:22px;font-weight:700}

/* footer */
.footer{top:4020px;height:381px;background:linear-gradient(180deg,#17181c,#0e0f12)}
.f-col{position:absolute;top:80px}
.f-col h4{color:var(--white);font-size:18px;font-weight:700;margin-bottom:26px}
.f-col li{list-style:none;color:#c8c8d0;font-size:15px;line-height:1.45}
.f-divider{position:absolute;top:70px;width:1px;height:190px;background:#3a3b42}
.socials{display:flex;gap:8px}
.social{width:32px;height:32px;border-radius:50%;background:var(--blue-bright)}
.social.red{background:#d23b3b}
.f-office{position:absolute;right:44px;top:80px;text-align:right;color:#c8c8d0;font-size:15px;line-height:1.45}
.f-office h4{color:var(--white);font-size:18px;margin-bottom:26px}
.f-brand{left:40px;top:232px;display:flex;align-items:center;gap:10px}
.f-brand .brand-name{color:#9a9aa4;font-size:22px}
.f-bottom{position:absolute;top:320px;left:0;width:100%;border-top:1px solid #2d2e34;padding-top:16px;text-align:center;color:#a0a0aa;font-size:13px}
</style>
</head>
<body>

<section class="hero">
  <svg class="hero-wave" viewBox="0 0 760 560" aria-hidden="true">
    <defs>
      <linearGradient id="waveGrad" x1="0" y1="0" x2="1" y2="1">
        <stop offset="0" stop-color="#1f4fa8"/>
        <stop offset=".55" stop-color="#3a2fa0"/>
        <stop offset="1" stop-color="#7a1fa0"/>
      </linearGradient>
    </defs>
    <path d="M120 0 C 160 130 150 260 300 300 C 430 335 470 250 560 330 C 640 400 620 500 760 545 L760 0 Z" fill="url(#waveGrad)"/>
  </svg>

  <div class="abs brand">
    <div class="brand-mark"></div>
    <div>
      <div class="brand-name">Kovel Digital</div>
    </div>
  </div>
  <div class="abs phone">
    <svg width="16" height="16" viewBox="0 0 24 24" aria-hidden="true"><path d="M6.6 10.8c1.4 2.8 3.8 5.1 6.6 6.6l2.2-2.2c.3-.3.7-.4 1-.2 1.1.4 2.3.6 3.6.6.6 0 1 .4 1 1V20c0 .6-.4 1-1 1C10.6 21 3 13.4 3 4c0-.6.4-1 1-1h3.5c.6 0 1 .4 1 1 0 1.3.2 2.5.6 3.6.1.3 0 .7-.2 1L6.6 10.8z" fill="#555"/></svg>
    +44 (0) 1632 960418
  </div>
  <nav class="abs nav">
    <a href="#">HOME</a>
    <a href="#">SERVICES ▾</a>
    <a href="#">WHITE LABEL LINK BUILDING</a>
    <a href="#" class="nav-cta">CONTACT US</a>
  </nav>

  <div class="hero-device" role="img" aria-label="Smartphone showing the brand on a lime patterned screen"></div>

  <h1 class="abs hero-title">Search Marketing<br>That Actually Delivers</h1>
  <p class="abs hero-lead">Search marketing is our forte. Our client results highlight just how good we do it</p>
  <a href="#" class="abs btn btn-quote">REQUEST A QUOTE</a>
  <a href="#" class="abs btn btn-how">HOW IT WORKS?</a>

  <h2 class="abs roi-title">Do you want to see an enviable<br>ROI on search marketing?</h2>
  <p class="abs roi-kicker">IT'S POSSIBLE – YOU'VE FOUND US.</p>
  <p class="abs roi-body">We know and understand the world of business. We know that ROI is the single most important metric in the marketing world. We've worked within some of the world's largest industries – such as finance, insurance, payday loans and health; where achieving above 100% ROI is often impossible. For us, it's just a challenge that can be overcome. Whether we're working with you to drive your Pay-Per-Click Marketing, Organic Search Marketing (SEO), Email Marketing or Lead Filtering &amp; Delivery – we always have your ROI in mind. That's why we're known as the ROI driven digital agency.</p>
  <p class="abs roi-handle"><b>Handle your SEO in-house?</b> Consider using our industry-leading link outreach service to bolster your efforts.</p>
  <div class="abs roi-accent"></div>
  <div class="abs roi-image" role="img" aria-label="Desktop computer with monitor and tower"></div>
  <div class="abs badges" aria-label="Partner badges">
    <div class="badge"></div><div class="badge"></div><div class="badge"></div>
    <div class="badge"></div><div class="badge"></div><div class="badge"></div>
  </div>
</section>

<section class="services" role="region" aria-label="City skyline at night behind the services">
  <p class="abs services-kicker">Start managing your business</p>
  <h2 class="abs services-title">Introducing New Services</h2>

  <div class="card" style="left:226px;top:270px">
    <div class="card-icon" role="img" aria-label="Organic search icon"></div>
    <h3>Organic Search</h3>
    <p>Attract traffic that converts and interacts with your brand through Organic. We implement both short-term and long-term campaigns to bolster your success.</p>
    <span class="more">Read More</span>
  </div>
  <div class="card" style="left:813px;top:270px">
    <div class="card-icon" role="img" aria-label="Paid search icon"></div>
    <h3>Paid Search</h3>
    <p>Drive highly converting traffic to your website. Our PPC campaigns are ROI-driven from the start – helping you to scale your business quickly.</p>
    <span class="more">Read More</span>
  </div>
  <div class="card" style="left:226px;top:512px">
    <div class="card-icon" role="img" aria-label="Link outreach icon"></div>
    <h3>Link Outreach</h3>
    <p>The core foundation of any search campaign. Our team of link outreachers are the best in the industry. We secure link placements that drive rankings.</p>
    <span class="more">Read More</span>
  </div>
  <div class="card" style="left:813px;top:512px">
    <div class="card-icon" role="img" aria-label="UX and CRO icon"></div>
    <h3>UX &amp; CRO</h3>
    <p>Attract traffic that converts and interacts with your brand through Organic. We implement both short-term and long-term campaigns to bolster your success.</p>
    <span class="more">Read More</span>
  </div>
  <div class="card" style="left:226px;top:755px">
    <div class="card-icon" role="img" aria-label="Email marketing icon"></div>
    <h3>Email Marketing</h3>
    <p>Our targeted email marketing campaigns allow you to segment users and deliver custom tailored campaigns and promotions to different demographics.</p>
    <span class="more">Read More</span>
  </div>
  <div class="card" style="left:813px;top:755px">
    <div class="card-icon" role="img" aria-label="Social media icon"></div>
    <h3>Social Media</h3>
    <p>Attract traffic that converts and interacts with your brand through Organic. We implement both short-term and long-term campaigns to bolster your success.</p>
    <span class="more">Read More</span>
  </div>
</section>

<section class="grow">
  <h2 class="abs grow-title">We Grow As Our Clients Grow</h2>
  <p class="abs grow-kicker">THAT'S WHAT WE LOVE</p>
  <div class="abs grow-photo" role="img" aria-label="Team joining hands over a desk with laptops"></div>
  <div class="abs grow-text">
    <p>Over 40,000 searches are made every single minute on Searchly. We're here to help you start capturing traffic that interacts with your brand and converts.</p>
    <p>Search marketing is our forte. Our client results highlight just how good we do it.</p>
  </div>
  <div class="abs stats">
    <div class="stat"><b>117</b><span>SATISFIED<br>CLIENTS</span></div>
    <div class="stat"><b>215</b><span>CAMPAIGNS<br>FINISHED</span></div>
    <div class="stat"><b>1,798</b><span>CUPS OF COFFEE</span></div>
    <div class="stat-tick">
      <svg width="64" height="50" viewBox="0 0 64 50" aria-hidden="true"><path d="M4 26 L22 44 L60 6" fill="none" stroke="#111" stroke-width="9"/></svg>
    </div>
  </div>
</section>

<section class="handle">
  <h2 class="abs handle-title">Handle SEO Yourself? Perfect.</h2>
  <p class="abs handle-kicker">HASSLE-FREE LINK PLACEMENTS THAT DRIVE RANKINGS</p>
  <div class="abs handle-photo" role="img" aria-label="Business team celebrating with raised arms"></div>
  <div class="abs click-box">
    <strong>JUST CLICK HERE.</strong>
    <span>IF YOU WANT TO LEARN MORE<br>AND GET OUR PRICING!</span>
  </div>
  <div class="abs click-arrow">
    <svg width="44" height="56" viewBox="0 0 44 56" aria-hidden="true"><path d="M6 4 L34 28 L6 52" fill="none" stroke="#111" stroke-width="10"/></svg>
  </div>
  <div class="abs handle-text">
    <p>Our link placements are used by some of the world's largest companies in the most difficult industries – such as payday loans, insurance, finance, health and legal. We use our link placement service in conjunction with our Organic Search (SEO) offerings; although some of our clients handle their SEO in-house and prefer to use our link placements to bolster their rankings.</p>
    <p>Here's how our unique, link acquisition process works:</p>
    <p>We take your clients URLs and their business sector (or your own sites), and we utilise our connections to try and secure a link placement.<br>All of the sites we outreach too are 100% genuine – we do not own nor control any of the sites.<br>If a webmaster chooses to link to you, it is of their own accord. They have decided to link to you. Thus, you have earned a genuine link.<br>We will identify the most relevant page/post on their site, and work with the webmaster to weave your links into their existing content. We will write an additional sentence or two to make sure the anchor text fits in with the content.</p>
  </div>
</section>

<section class="cta">
  <h2>WANT TO IMPROVE YOUR ROI? LET'S TALK</h2>
  <p>We'll never turn down an opportunity to discover how we can help grow your business.</p>
  <a href="#" class="btn btn-contact">CONTACT US TODAY</a>
</section>

<footer class="footer" role="contentinfo">
  <div class="f-col" style="left:40px">
    <h4>Our Key Services</h4>
    <ul><li>Link Outreach</li><li>Organic Search (SEO)</li><li>Paid Search (PPC)</li><li>Social Media Marketing</li></ul>
  </div>
  <div class="f-divider" style="left:264px"></div>
  <div class="f-col" style="left:292px">
    <h4>Locations We Cover (SEO)</h4>
    <ul><li>Birmingham</li><li>Essex</li><li>London</li><li>Manchester</li><li>Stoke-on-Trent</li><li>➜ See All Locations We Cover (SEO)</li></ul>
  </div>
  <div class="f-divider" style="left:608px"></div>
  <div class="f-col" style="left:640px">
    <h4>Connect With Us</h4>
    <div class="socials">
      <span class="social"></span><span class="social"></span><span class="social red"></span>
      <span class="social"></span><span class="social"></span><span class="social red"></span>
    </div>
  </div>
  <div class="f-divider" style="left:888px"></div>
  <div class="f-office">
    <h4>Shrewsbury Office</h4>
    Kovel Digital Ltd, The Granary,<br>14 Harlow Mill Lane<br>Shrewsbury<br>SY9 4QX<br><br>Phone: 01632 960418<br>Email: info@koveldigital-studio.net
  </div>
  <div class="abs f-brand">
    <div class="brand-mark" style="background:#6a6a74"></div>
    <div class="brand-name">Kovel Digital</div>
  </div>
  <p class="f-bottom">© 2018 Kovel Digital Limited. All rights reserved.</p>
</footer>

</body>
</html>
```